Business Card design for an International Import Export House

We need a Business Card design for our import export business. We trade in Minerals, Metals, Rice, Sugar, Steel etc.. The design should be minimalistic. It may or may not contain the physical address. In case you want to include the physical address - 418 Marwick Plaza, Oakvale Sector 7, Rivermoor, Kestrel State, India, 560417.

Target Market(s)

Steel Mills or Steel Plants, Factories, Mining businesses, Industrial houses, Government Agencies

Industry/Entity Type

Importer

Contact Information for Business Card

Business Name - Verrano Trade

Font styles to use
Other font styles liked:
• montserrat

Requirements
Must have
• Darin Pohlak - President
• www.verranotrade.example
• darin@verranotrade.example
• +91-988-412-3675
Nice to have
• worldwide suppliers of ores

```html
<!DOCTYPE html>
<html lang="en">
<head>
<meta charset="utf-8">
<title>Verrano Trade – Business Card</title>
<link rel="stylesheet" href="https://fonts.googleapis.com/css2?family=Montserrat:wght@400;500;700&display=swap">
<style>
  :root {
    --teal: #3f8ca7;
    --white: #ffffff;
    --ink: #16191b;
    --stage: #e9ebec;
    --card-w: 540px;
    --card-h: 309px;
  }
  * { box-sizing: border-box; margin: 0; padding: 0; }
  html, body {
    width: 1200px; height: 780px; overflow: hidden;
    background: var(--stage);
    font-family: "Montserrat", Arial, sans-serif;
  }
  .sheet {
    width: 1200px; height: 780px;
    display: flex; align-items: center; justify-content: center; gap: 40px;
  }
  .card {
    position: relative;
    width: var(--card-w); height: var(--card-h);
    overflow: hidden;
    box-shadow: 0 6px 18px rgba(0,0,0,.18);
  }
  /* Back side */
  .card--back {
    background: var(--teal);
    display: flex; align-items: center; justify-content: center;
  }
  .brand {
    display: flex; align-items: center; gap: 9px;
    font-weight: 700; text-transform: uppercase; letter-spacing: .5px;
    white-space: nowrap;
  }
  .brand__dot { display: block; border-radius: 50%; flex: none; }
  .card--back .brand { color: var(--white); font-size: 26px; }
  .card--back .brand__dot { width: 22px; height: 22px; background: var(--white); }

  /* Front side */
  .card--front { background: var(--white); }
  .card__bg { position: absolute; inset: 0; }
  .card--front .brand {
    position: absolute; left: 40px; top: 140px;
    color: var(--teal); font-size: 18px;
  }
  .card--front .brand__dot { width: 16px; height: 16px; background: var(--teal); }

  .details {
    position: absolute; left: 330px; top: 38px; right: 16px;
    color: var(--white);
  }
  .person__name {
    font-size: 17px; font-weight: 700; text-transform: uppercase; letter-spacing: 1px;
    line-height: 1.1;
  }
  .person__role { font-size: 11px; font-weight: 500; margin-top: 2px; }
  .address {
    font-style: normal; font-size: 11px; line-height: 1.45; font-weight: 500;
    margin-top: 36px;
  }
  .contacts { list-style: none; margin-top: 18px; }
  .contacts li {
    display: flex; align-items: center; gap: 7px;
    font-size: 11px; font-weight: 500; line-height: 1; margin-bottom: 5px;
    white-space: nowrap;
  }
  .contacts svg { flex: none; width: 13px; height: 13px; }
</style>
</head>
<body>
<main class="sheet">

  <section class="card card--back" aria-label="Card back">
    <div class="brand"><span class="brand__dot"></span>Verrano Trade</div>
  </section>

  <section class="card card--front" aria-label="Card front">
    <svg class="card__bg" viewBox="0 0 540 309" width="540" height="309" aria-hidden="true">
      <path d="M322 0 C290 70 300 200 196 309 L540 309 L540 0 Z" fill="var(--teal)"/>
      <path d="M300 130 C296 215 262 282 178 309 L212 309 C276 280 302 222 300 130 Z" fill="var(--ink)"/>
    </svg>

    <div class="brand"><span class="brand__dot"></span>Verrano Trade</div>

    <div class="details">
      <p class="person__name">Darin Pohlak</p>
      <p class="person__role">President</p>
      <address class="address">
        418 Marwick Plaza,<br>
        Oakvale Sector 7, Rivermoor<br>
        Kestrel State, India, 560417.
      </address>
      <ul class="contacts">
        <li>
          <svg viewBox="0 0 13 13"><rect width="13" height="13" rx="2" fill="var(--ink)"/><path d="M4 3 L5.5 3 L6 5 L5 5.8 C5.5 7 6 7.5 7.2 8 L8 7 L10 7.5 L10 9 C10 9.5 9.5 10 9 10 C6 10 3 7 3 4 C3 3.5 3.5 3 4 3 Z" fill="var(--white)"/></svg>
          +91-988-412-3675
        </li>
        <li>
          <svg viewBox="0 0 13 13"><rect width="13" height="13" rx="2" fill="var(--ink)"/><rect x="2.5" y="4" width="8" height="5.5" fill="none" stroke="var(--white)" stroke-width="1"/><path d="M2.5 4 L6.5 7 L10.5 4" fill="none" stroke="var(--white)" stroke-width="1"/></svg>
          darin@verranotrade.example
        </li>
        <li>
          <svg viewBox="0 0 13 13"><rect width="13" height="13" rx="2" fill="var(--ink)"/><circle cx="6.5" cy="6.5" r="4" fill="none" stroke="var(--white)" stroke-width=".9"/><ellipse cx="6.5" cy="6.5" rx="1.8" ry="4" fill="none" stroke="var(--white)" stroke-width=".8"/><path d="M2.5 6.5 H10.5" stroke="var(--white)" stroke-width=".8"/></svg>
          www.verranotrade.example
        </li>
      </ul>
    </div>
  </section>

</main>
</body>
</html>
```